Harrowgate Construction And Masonry Ltd

Black background

Logo - attached

Services (bullet points)
New Builds
Extensions
Refurbishments
Alterations
Brickwork Specialists

Contact details - 01632 960418 or 0791 5530274

Email address - contact@harrowgateconstructionandmasonry.co.uk

Website - www.harrowgateconstructionandmasonry.co.uk

Facebook logo

```html
<!DOCTYPE html>
<html lang="en">
<head>
<meta charset="utf-8">
<title>Harrowgate Construction And Masonry Ltd – Flyer</title>
<link href="https://fonts.googleapis.com/css2?family=Montserrat:wght@400;500;600;700;800;900&family=Oswald:wght@600;700&display=swap" rel="stylesheet">
<style>
  :root{
    --green:#3dba5f;
    --green-dark:#2fa34f;
    --ink:#1c1f1e;
    --bar:#262826;
    --paper:#f3f3f3;
    --panel-top:#ffffff;
    --panel-bottom:#e6e6e6;
    --sky:#4b8fd6;
    --canvas:#d4d4d4;
  }
  *{box-sizing:border-box;margin:0;padding:0}
  html,body{width:1200px;height:2682px;overflow:hidden;background:var(--canvas)}
  .flyer{
    position:absolute;left:50px;top:563px;width:810px;height:1145px;
    transform:scale(1.358);transform-origin:0 0;
    background:var(--paper);overflow:hidden;
    font-family:'Montserrat',sans-serif;color:var(--ink);
    box-shadow:0 2px 6px rgba(0,0,0,.15);
  }
  .hero-photo{
    position:absolute;left:0;top:0;width:810px;height:640px;
    background:linear-gradient(180deg,#3f86d2 0%,#8fc0ec 30%,#c9b49a 45%,#b9a184 60%,#d9c9aa 75%,#6fa848 88%,#5f9a3e 100%);
  }
  .top-panel{
    position:absolute;left:23px;top:0;width:767px;height:250px;
    background:linear-gradient(180deg,var(--panel-top),var(--panel-bottom));
    border-radius:0 0 40px 40px;
  }
  .brand{
    position:absolute;left:40px;top:52px;width:260px;text-align:center;
  }
  .brand-mark{width:34px;height:34px;background:var(--green);margin:0 auto 14px}
  .brand-name{font-size:22px;font-weight:700;line-height:1.2;color:var(--ink)}
  .headline{position:absolute;left:333px;top:60px;width:457px}
  .headline-band{
    height:55px;padding-left:26px;font-size:45px;font-weight:900;color:#fff;
    line-height:55px;letter-spacing:.5px;
  }
  .headline-band.green{background:var(--green)}
  .headline-band.black{background:var(--ink);margin-top:5px}
  .headline-tail{padding-left:26px;font-size:47px;font-weight:500;line-height:62px;color:var(--ink)}
  .curve{position:absolute;left:0;top:568px;width:810px;height:80px}
  .services-title{
    position:absolute;left:0;top:618px;width:810px;text-align:center;
    font-family:'Oswald',sans-serif;font-weight:700;font-size:38px;line-height:50px;
  }
  .services-title .accent{color:var(--green)}
  .services-title::before,.services-title::after{
    content:"";display:inline-block;width:50px;height:2px;background:var(--ink);
    vertical-align:middle;margin:0 16px;
  }
  .service-card{
    position:absolute;width:226px;height:140px;border:2px solid var(--ink);
    border-radius:14px;overflow:hidden;background:var(--ink);
  }
  .service-photo{height:95px}
  .service-label{
    height:43px;line-height:40px;text-align:center;color:var(--green);
    font-weight:700;font-size:18px;
  }
  .ph-newbuild{background:linear-gradient(180deg,#a9cdee 0%,#dfe9f1 45%,#c99b55 70%,#6b6b6b 100%)}
  .ph-extension{background:linear-gradient(135deg,#6a8d4f 0%,#b58a63 45%,#d8d3cc 75%,#7b7b7b 100%)}
  .ph-refurb{background:linear-gradient(180deg,#e7e7e7 0%,#8d8d8d 50%,#5c5c5c 100%)}
  .ph-alteration{background:linear-gradient(135deg,#7a4a35 0%,#d7b065 40%,#e9cf86 70%,#9a7444 100%)}
  .ph-brickwork{background:linear-gradient(180deg,#6f8f5a 0%,#9b4b36 45%,#6b6e6c 80%,#4d4f4e 100%)}
  .phone-band{
    position:absolute;left:0;top:1005px;width:810px;height:85px;background:var(--green);
    display:flex;align-items:center;
  }
  .phone-icon{margin-left:55px;width:42px;height:42px}
  .phone-numbers{margin-left:18px;font-size:39px;font-weight:700;color:#fff;letter-spacing:.5px}
  .contact-bar{
    position:absolute;left:0;top:1090px;width:810px;height:55px;background:var(--bar);
    display:flex;align-items:center;justify-content:center;gap:10px;
    color:#fff;font-size:12px;font-weight:700;
  }
  .contact-item{display:flex;align-items:center;gap:7px}
  .divider{width:1px;height:20px;background:#8a8a8a;margin:0 4px}
  .social-dot{width:20px;height:20px;border-radius:50%;background:var(--green)}
</style>
</head>
<body>
<main class="flyer">
  <div class="hero-photo" role="img" aria-label="Photo of a modern single-storey house with stone-clad entrance, double garage, trees and lawn under a blue sky"></div>

  <header class="top-panel">
    <div class="brand">
      <div class="brand-mark"></div>
      <div class="brand-name">Harrowgate Construction And Masonry Ltd</div>
    </div>
    <div class="headline">
      <div class="headline-band green">BUILDING AND</div>
      <div class="headline-band black">BRICKWORK</div>
      <div class="headline-tail">SPECIALIST’S</div>
    </div>
  </header>

  <svg class="curve" viewBox="0 0 810 80" aria-hidden="true">
    <path d="M0 52 Q405 -8 810 52 L810 80 L0 80 Z" fill="#f3f3f3"/>
    <path d="M0 52 Q405 -8 810 52" fill="none" stroke="#3dba5f" stroke-width="4"/>
  </svg>

  <h2 class="services-title"><span class="accent">OUR</span> SERVICES</h2>

  <section class="service-card" style="left:57px;top:685px">
    <div class="service-photo ph-newbuild" role="img" aria-label="Photo of timber roof framing on a new build"></div>
    <div class="service-label">New Builds</div>
  </section>
  <section class="service-card" style="left:293px;top:685px">
    <div class="service-photo ph-extension" role="img" aria-label="Photo of a house extension under construction"></div>
    <div class="service-label">Extensions</div>
  </section>
  <section class="service-card" style="left:528px;top:685px">
    <div class="service-photo ph-refurb" role="img" aria-label="Photo of a refurbished grey kitchen"></div>
    <div class="service-label">Refurbishments</div>
  </section>
  <section class="service-card" style="left:167px;top:840px">
    <div class="service-photo ph-alteration" role="img" aria-label="Photo of roof timbers during an alteration"></div>
    <div class="service-label">Alterations</div>
  </section>
  <section class="service-card" style="left:403px;top:840px">
    <div class="service-photo ph-brickwork" role="img" aria-label="Photo of new brick pillars and walls"></div>
    <div class="service-label">Brickwork Specialists</div>
  </section>

  <div class="phone-band">
    <svg class="phone-icon" viewBox="0 0 42 42" aria-hidden="true">
      <circle cx="21" cy="21" r="19" fill="none" stroke="#1c1f1e" stroke-width="2.5"/>
      <path d="M14 12 l4 0 l2 5 l-3 2 q2 4 6 6 l2 -3 l5 2 l0 4 q-1 2 -3 2 q-10 -1 -15 -13 q0 -3 2 -5 z" fill="#1c1f1e"/>
    </svg>
    <div class="phone-numbers">01632 960418 or 0791 5530274</div>
  </div>

  <footer class="contact-bar">
    <div class="contact-item">
      <svg width="14" height="11" viewBox="0 0 14 11" aria-hidden="true"><rect width="14" height="11" rx="1.5" fill="#3dba5f"/><path d="M1 1.5 L7 6 L13 1.5" fill="none" stroke="#262826" stroke-width="1.4"/></svg>
      <span>contact@harrowgateconstructionandmasonry.co.uk</span>
    </div>
    <div class="divider"></div>
    <div class="contact-item">
      <svg width="15" height="15" viewBox="0 0 16 16" aria-hidden="true"><circle cx="8" cy="8" r="7" fill="none" stroke="#3dba5f" stroke-width="1.5"/><ellipse cx="8" cy="8" rx="3" ry="7" fill="none" stroke="#3dba5f" stroke-width="1.2"/><path d="M1 8 H15" stroke="#3dba5f" stroke-width="1.2"/></svg>
      <span>www.harrowgateconstructionandmasonry.co.uk</span>
    </div>
    <div class="divider"></div>
    <div class="social-dot" role="img" aria-label="Social media link"></div>
  </footer>
</main>
</body>
</html>
```